Makeup artist looking for business card design

- Business card to be memorable and recognisable

- I've attached photos of my logo (File 4), photos that I want to incorporate into the design (File 5,6 & 7) and an example of the design I like "Dora Tully" (File 1)

- I've attached 3 photos of the designs I want to use, please use one of your choice

- Next to Instagram (File 2) and Facebook (File 3), please use their logo.

- No coloured background, either use the original background (grey) old white.

- Please include the following on the business card:
- Business name: LK Beauty Studio
- My name: Maribel Oste
- Occupation: Makeup Artist
- Contact number: 0455 392 718
- Email: maribeloste_beauty@examplemail.net
- Instagram (please use image): @lkbeautystudio
- Facebook (please use image): www.facebook-example.net/LKBeautyStudio

Target Market(s)

Target woman for bridal makeup, occasion, fashion makeup and print.

Industry/Entity Type

Business

Requirements
Must have
• Logo provided and photo provided
Should not have
• Colourful background
Too cluttered
Shouldn't use old style font

```html
<!DOCTYPE html>
<html lang="en">
<head>
<meta charset="utf-8">
<title>LK Beauty Studio – Business Card</title>
<link href="https://fonts.googleapis.com/css2?family=Michroma&display=swap" rel="stylesheet">
<style>
  :root {
    --stage: #2e261e;
    --paper: #e7e6e6;
    --paper-edge: #d6d5d5;
    --ink: #1e1e1e;
    --ink-soft: #3a3a3a;
    --rose: #d9bcb6;
    --rose-deep: #b89690;
    --band-dark: #8a8a8a;
    --band-light: #f1f1f1;
    --photo-pink: #e7a9a6;
    --photo-violet: #8c4a8c;
    --photo-lilac: #c9a6cf;
    --photo-white: #ece8ee;
  }
  * { box-sizing: border-box; margin: 0; padding: 0; }
  html, body {
    width: 1200px; height: 1000px; overflow: hidden;
    background: var(--stage);
    font-family: "Michroma", "Arial", sans-serif;
  }
  .card {
    position: absolute; top: 140px;
    width: 420px; height: 720px;
    overflow: hidden;
    box-shadow: 0 10px 30px rgba(0,0,0,.45);
  }
  /* Front */
  .card--front { left: 150px; }
  .front-photo {
    position: absolute; inset: 0;
    background:
      radial-gradient(ellipse at 55% 22%, var(--photo-pink) 0 28%, transparent 55%),
      radial-gradient(ellipse at 70% 60%, var(--photo-white) 0 12%, transparent 40%),
      linear-gradient(160deg, var(--photo-lilac) 0%, var(--photo-violet) 55%, var(--photo-lilac) 80%, var(--photo-white) 100%);
  }
  .front-brand {
    position: absolute; left: 34px; bottom: 250px;
    display: flex; align-items: center; gap: 10px;
    font-size: 14px; letter-spacing: 1px; text-transform: uppercase;
    color: var(--ink);
  }
  .brand-dot {
    width: 12px; height: 12px; border-radius: 50%; background: var(--ink); flex: none;
  }
  /* Back */
  .card--back { left: 630px; background: var(--paper); border: 1px solid var(--paper-edge); }
  .back-brand {
    position: absolute; top: 170px; left: 0; right: 0;
    display: flex; justify-content: center; align-items: center; gap: 12px;
    font-size: 17px; letter-spacing: 1.5px; text-transform: uppercase;
    color: var(--ink);
  }
  .name-band {
    position: absolute; top: 300px; left: 0; right: 0; height: 62px;
    background: linear-gradient(90deg, var(--band-dark) 0%, #bdbdbd 40%, var(--band-light) 100%);
  }
  .name-box {
    position: absolute; top: 306px; left: 56px; right: 18px; height: 50px;
    background: var(--ink-soft);
    border: 2px solid var(--rose-deep);
    display: flex; align-items: center; justify-content: center;
    font-size: 24px; letter-spacing: 1px; color: var(--rose);
    text-transform: uppercase; white-space: nowrap;
  }
  .role-box {
    position: absolute; top: 364px; left: 24px; width: 300px; height: 40px;
    background: var(--rose);
    border: 2px solid var(--ink-soft);
    display: flex; align-items: center; justify-content: center;
    font-size: 19px; color: var(--ink); text-transform: uppercase; white-space: nowrap;
  }
  .contact-list {
    position: absolute; top: 440px; left: 24px; right: 20px;
    list-style: none;
  }
  .contact-item {
    display: flex; align-items: center; gap: 10px;
    height: 40px;
    font-size: 9.5px; letter-spacing: .2px; color: var(--ink);
    text-transform: uppercase; white-space: nowrap;
  }
  .contact-item--phone { font-size: 17px; letter-spacing: 2px; }
  .contact-icon { width: 24px; height: 24px; flex: none; }
  .social-square { width: 22px; height: 22px; margin: 0 1px; flex: none; background: var(--ink-soft); border-radius: 3px; }
</style>
</head>
<body>
  <section class="card card--front">
    <div class="front-photo" role="img" aria-label="Beauty portrait of a model with violet lipstick framed by large purple and white flower petals"></div>
    <div class="front-brand"><span class="brand-dot"></span>LK Beauty Studio</div>
  </section>

  <section class="card card--back">
    <div class="back-brand"><span class="brand-dot"></span>LK Beauty Studio</div>
    <div class="name-band"></div>
    <div class="name-box">Maribel Oste</div>
    <div class="role-box">Makeup Artist</div>
    <ul class="contact-list">
      <li class="contact-item contact-item--phone">
        <svg class="contact-icon" viewBox="0 0 24 24" aria-hidden="true">
          <path d="M6.6 10.8a15.1 15.1 0 0 0 6.6 6.6l2.2-2.2a1 1 0 0 1 1-.25 11.4 11.4 0 0 0 3.6.57 1 1 0 0 1 1 1V20a1 1 0 0 1-1 1A17 17 0 0 1 3 4a1 1 0 0 1 1-1h3.5a1 1 0 0 1 1 1c0 1.25.2 2.45.57 3.57a1 1 0 0 1-.25 1z" fill="var(--rose-deep)"/>
        </svg>
        0455 392 718
      </li>
      <li class="contact-item">
        <svg class="contact-icon" viewBox="0 0 24 24" aria-hidden="true">
          <rect x="2" y="5" width="20" height="14" rx="1.5" fill="var(--rose)" stroke="var(--rose-deep)" stroke-width="1.2"/>
          <path d="M2.5 5.5 12 13l9.5-7.5M2.5 18.5l7-6M21.5 18.5l-7-6" fill="none" stroke="var(--rose-deep)" stroke-width="1.2"/>
        </svg>
        maribeloste_beauty@examplemail.net
      </li>
      <li class="contact-item"><span class="social-square"></span>@lkbeautystudio</li>
      <li class="contact-item"><span class="social-square"></span>/LKBeautyStudio</li>
    </ul>
  </section>
</body>
</html>
```